Unique Elegant Stationary Set

Prepare a unique eye catching stationary set consisting of :
(1) Letterhead
(2) A3 Envelope
(3) Business Card
(4) Email Signature Banner

Package to be elegant, modern, and designers not only to think of design or colors but also materials could make a big difference, embossing, debossing, glossy, matt ....etc.

I attached both our new logos (Stacked or Linear) noting you may use any of them but you cant modify anything in the logos. Also attached our final draft portfolio to see what type of projects we work on and i also have here a glimboard page link showing the direction we want: https://www.glimboard.example/ravelkoton/business-card-design/

Target Market(s)

VVIP / Elite Developers

Industry/Entity Type

Architecture

Font styles to use
Sans Serif
Other font styles liked:
• unitext

Requirements
Should not have
• too many colors, or being busy in general. We want something pleasing to the eye

```html
<!DOCTYPE html>
<html lang="en">
<head>
<meta charset="utf-8">
<title>Norvane Design – Business Card</title>
<link rel="stylesheet" href="https://fonts.googleapis.com/css2?family=Lato:wght@400;700&display=swap">
<style>
  :root {
    --bg: #4b4b4d;
    --card: #aea4af;
    --ink: #3b373e;
    --ink-soft: #4a4550;
    --mark: #ece6ee;
    --rule: #57525b;
  }
  * { box-sizing: border-box; margin: 0; padding: 0; }
  html, body { width: 1200px; height: 694px; overflow: hidden; }
  body {
    background: var(--bg);
    font-family: "Lato", sans-serif;
    color: var(--ink);
    position: relative;
  }
  .card {
    position: absolute;
    top: 192px;
    width: 530px;
    height: 310px;
    background: var(--card);
    border-radius: 3px;
    box-shadow: 0 14px 34px rgba(0,0,0,.35);
  }
  .card--front { left: 50px; }
  .card--back { left: 620px; }

  .brand {
    font-weight: 700;
    color: var(--mark);
    text-transform: uppercase;
    line-height: 1;
    display: flex;
    align-items: center;
    gap: 12px;
  }
  .brand__square {
    width: 14px;
    height: 14px;
    background: var(--mark);
  }
  .card--front .brand {
    position: absolute;
    inset: 0;
    justify-content: center;
    font-size: 34px;
    letter-spacing: 8px;
  }
  .card--back .brand {
    position: absolute;
    right: 36px;
    top: 46px;
    font-size: 22px;
    letter-spacing: 5px;
  }
  .card--back .brand__square { width: 10px; height: 10px; }

  .rule {
    position: absolute;
    height: 1px;
    background: var(--rule);
  }
  .rule--top { left: 36px; right: 36px; top: 116px; }
  .rule--name { left: 36px; width: 200px; top: 196px; }

  .person { position: absolute; left: 36px; top: 138px; }
  .person__name {
    font-size: 21px;
    font-weight: 700;
    letter-spacing: .5px;
    color: var(--ink);
  }
  .person__role {
    font-size: 13px;
    margin-top: 4px;
    color: var(--ink-soft);
  }

  .contacts {
    position: absolute;
    left: 36px;
    top: 210px;
    list-style: none;
  }
  .contacts li {
    display: flex;
    align-items: center;
    gap: 10px;
    font-size: 13px;
    color: var(--ink-soft);
    height: 24px;
  }
  .contacts svg { width: 13px; height: 13px; fill: var(--ink); }

  .address {
    position: absolute;
    right: 36px;
    top: 138px;
    text-align: right;
    font-size: 13px;
    line-height: 20px;
    color: var(--ink-soft);
  }
</style>
</head>
<body>

  <section class="card card--front" aria-label="Business card front">
    <div class="brand"><span class="brand__square"></span>Norvane Design</div>
  </section>

  <section class="card card--back" aria-label="Business card back">
    <div class="brand"><span class="brand__square"></span>Norvane Design</div>
    <div class="rule rule--top"></div>

    <div class="person">
      <p class="person__name">CALLUM BRIGHTWATER</p>
      <p class="person__role">Managing Director</p>
    </div>
    <div class="rule rule--name"></div>

    <ul class="contacts">
      <li>
        <svg viewBox="0 0 16 16" aria-hidden="true"><path d="M3.6 1.2l2.3 2.6-1.3 1.8c.9 2 2.6 3.7 4.6 4.6l1.8-1.3 2.6 2.3-1.4 2.6C7.2 13.5 2.5 8.8 1 3.8z"/></svg>
        044-987 210 456
      </li>
      <li>
        <svg viewBox="0 0 16 16" aria-hidden="true"><path d="M1 3h14v10H1z M1.5 3.5L8 9l6.5-5.5" fill="none" stroke="#3b373e" stroke-width="1.6"/><path d="M1 3h14L8 8.5z"/></svg>
        hello@norvane.example
      </li>
      <li>
        <svg viewBox="0 0 16 16" aria-hidden="true"><circle cx="8" cy="8" r="7"/><path d="M4 5.5c1.5-.5 2.5.5 3 1.5s-1 2-.5 3.5M10 3.5c0 1.5 1.5 2 2.5 2M9.5 12c.5-1.5 2-1.5 2.5-3" stroke="#aea4af" stroke-width="1.2" fill="none"/></svg>
        www.norvane.example
      </li>
    </ul>

    <p class="address">17, Harlow Crescent Avenue<br>30815, Estavia</p>
  </section>

</body>
</html>
```